DL flyer front and back + magnet

DL Flyer Design Brief – VKD Plumbing

Objective:
Create a bold, high-impact DL flyer promoting a Blocked Drain Special to generate immediate service calls.

Main Headline (Large & Eye Catching)

🚨 BLOCKED DRAIN SPECIAL – $299 🚨

High Pressure Water Jetting

Offer Details

💧 Clear stubborn blocked drains fast
💧 Professional high-pressure water jetting
💧 Removes tree roots, grease & debris

Limited Time Bonus

⭐ FIRST 15 CALLS RECEIVE A FREE CCTV CAMERA INSPECTION
(Valued at $149)

Trust Points (Icons or Ticks)

✔ Local Licensed Plumbers
✔ Fast Same Day Service
✔ Upfront Pricing
✔ 5 Star Rated Service

Call To Action (Very Prominent)

📞 CALL NOW TO BOOK
Limited bookings available

Phone: 0491 570 006
Website: vkdplumbing.com.au

Branding

Include:

VKD Plumbing logo

Plumbing imagery (blocked drain / jetting hose)

Use brand colours from VKD logo
💡 Design Tip:
The $299 price should be the biggest element on the flyer so people instantly see the offer.

Back Side Layout – VKD Plumbing Flyer
🏠 Your Local Trusted Plumber

Fast, Reliable Plumbing Services Across the Sutherland Shire

We provide professional plumbing services for homes and businesses including:

Our Services

✔ Blocked Drains
✔ Leak Detection & Repairs
✔ Hot Water Systems
✔ Tap & Toilet Repairs
✔ Stormwater Repairs
✔ CCTV Drain Inspections
✔ Gutter & Roof Plumbing
✔ Preventative Plumbing Maintenance

⭐ Why Choose VKD Plumbing?

✔ Fully Licensed & Insured
✔ Upfront Honest Pricing
✔ Fast Local Service
✔ Clean & Professional Workmanship
✔ Trusted by Local Homeowners & Businesses

⭐ What Our Customers Say

⭐⭐⭐⭐⭐
"Lachlan from VKD Plumbing cleared our blocked drain quickly and professionally. Highly recommend!"

⭐⭐⭐⭐⭐
"Prompt, reliable and great service. Will definitely use again."

(Fintaro Ratings)

📞 Need a Plumber?

VKD Plumbing

📞 Call: 0491 570 006
🌐 vkdplumbing.com.au

Add this small section on the back:

Neighbour Discount

💧 $59 OFF ANY PLUMBING REPAIR
(Mention this flyer when booking)

Magnet should be similar to these

```html
<!DOCTYPE html>
<html lang="en">
<head>
<meta charset="utf-8">
<title>VKD Plumbing – DL Flyer and Magnet</title>
<link rel="stylesheet" href="https://fonts.googleapis.com/css2?family=Montserrat:ital,wght@0,400;0,500;0,600;0,700;0,800;0,900;1,900&display=swap">
<style>
  :root {
    --stage: #9babc0;
    --blue: #2db9e3;
    --yellow: #f6c244;
    --ink: #2a2a2e;
    --white: #ffffff;
    --photo-navy: #33405a;
    --photo-light: #d9dde2;
    --steel: #b9c0c8;
  }
  * { box-sizing: border-box; margin: 0; padding: 0; }
  html, body { width: 1200px; height: 910px; overflow: hidden; }
  body {
    background: var(--stage);
    font-family: "Montserrat", sans-serif;
    color: var(--ink);
    position: relative;
  }
  .abs { position: absolute; }
  .stage-label {
    position: absolute;
    color: var(--white);
    font-weight: 500;
    font-size: 19px;
    letter-spacing: 3px;
    text-align: center;
    white-space: nowrap;
    transform: translateX(-50%);
  }
  .brand-name {
    color: var(--blue);
    font-weight: 900;
    line-height: 0.9;
    letter-spacing: -1px;
  }
  .brand-name .sub { display: block; letter-spacing: 1px; }

  /* Magnet */
  .magnet { left: 56px; top: 304px; width: 303px; height: 303px; filter: drop-shadow(0 6px 8px rgba(40,55,80,.25)); }
  .magnet-frame { position: absolute; left: 0; top: 0; }
  .magnet .brand-name { position: absolute; left: 0; right: 0; top: 44px; text-align: center; font-size: 44px; }
  .magnet .brand-name .sub { font-size: 16px; margin-top: 4px; }
  .magnet-band {
    position: absolute; left: 6px; right: 6px; top: 117px; height: 54px;
    background: var(--yellow); color: var(--white);
    font-weight: 800; font-size: 13.5px; line-height: 15px; text-align: center;
    display: flex; align-items: center; justify-content: center; letter-spacing: -.3px;
  }
  .magnet-cta { position: absolute; left: 0; right: 0; top: 186px; text-align: center; color: var(--blue); font-weight: 800; font-size: 16px; letter-spacing: -.5px; }
  .contact-line { position: absolute; display: flex; align-items: center; gap: 9px; white-space: nowrap; }
  .contact-line svg { flex: none; position: static; }
  .phone-number { font-weight: 600; letter-spacing: -.5px; }
  .web-address { font-weight: 500; }

  /* Flyers */
  .flyer { position: absolute; top: 69px; width: 364px; height: 771px; background: var(--white); overflow: hidden; box-shadow: 0 14px 18px -8px rgba(30,40,60,.35); }
  .flyer-front { left: 403px; }
  .flyer-back { left: 782px; }
  .photo, .illustration { position: absolute; }

  .front-logo { left: 28px; top: 34px; font-size: 56px; }
  .front-logo .sub { font-size: 20px; margin-top: 6px; }
  .headline-band { left: 0; top: 142px; width: 364px; height: 165px; background: var(--blue); }
  .headline { left: 26px; top: 158px; color: var(--white); font-weight: 900; font-size: 40px; line-height: 42px; letter-spacing: -2px; }
  .price-tag { left: 29px; top: 290px; width: 137px; height: 60px; background: var(--yellow); color: var(--white); font-weight: 900; font-size: 44px; letter-spacing: -2px; display: flex; align-items: center; justify-content: center; }
  .offer-box { left: 28px; top: 374px; width: 176px; height: 137px; border: 1px solid var(--yellow); padding: 16px 10px 0 13px; }
  .offer-title { font-weight: 800; font-size: 10.5px; line-height: 11px; letter-spacing: -.4px; margin-bottom: 9px; }
  .drop-list { list-style: none; }
  .drop-list li { position: relative; padding-left: 14px; font-size: 9.6px; line-height: 11.5px; margin-bottom: 4px; }
  .drop-list li::before { content: ""; position: absolute; left: 1px; top: 2px; width: 6px; height: 7px; background: var(--blue); border-radius: 50% 50% 50% 50% / 60% 60% 40% 40%; }
  .bonus-tab { left: 198px; top: 397px; width: 137px; height: 26px; background: var(--blue); color: var(--white); font-weight: 700; font-size: 10.5px; letter-spacing: -.4px; display: flex; align-items: center; justify-content: center; }
  .bonus-copy { left: 216px; top: 435px; font-size: 9.6px; line-height: 11.5px; font-weight: 500; }
  .bonus-value { left: 216px; top: 477px; font-size: 14px; font-weight: 700; letter-spacing: -.4px; }
  .trust-badge { position: absolute; display: flex; align-items: center; gap: 7px; padding-left: 8px; font-size: 11px; line-height: 13px; border: 1px solid var(--blue); white-space: nowrap; letter-spacing: -.2px; }
  .trust-badge svg { flex: none; }
  .trust-badge.yellow { border-color: var(--yellow); }
  .cta-title { left: 132px; top: 665px; font-weight: 800; font-size: 15px; letter-spacing: -.5px; }
  .cta-note { left: 132px; top: 685px; font-size: 12px; color: var(--blue); font-weight: 500; }

  .tag-local { left: 36px; top: 33px; width: 108px; height: 30px; background: var(--blue); color: var(--white); font-weight: 800; font-size: 13px; display: flex; align-items: center; justify-content: center; transform: rotate(-3deg); letter-spacing: -.4px; }
  .tag-trusted { left: 28px; top: 67px; width: 148px; height: 29px; background: var(--yellow); color: var(--white); font-weight: 800; font-size: 12.5px; display: flex; align-items: center; justify-content: center; letter-spacing: -.4px; }
  .intro { left: 28px; top: 113px; width: 160px; font-size: 9.6px; line-height: 11.6px; }
  .intro p + p { margin-top: 9px; }
  .section-title { font-weight: 800; font-size: 12.5px; letter-spacing: -.6px; }
  .tick-list { list-style: none; }
  .tick-list li { position: relative; padding-left: 16px; font-size: 9.8px; line-height: 11.5px; margin-bottom: 5.3px; white-space: nowrap; }
  .tick-list li svg { position: absolute; left: 0; top: 1px; }
  .services { left: 28px; top: 290px; }
  .why-box { left: 178px; top: 241px; width: 157px; height: 181px; border: 1px solid var(--blue); padding: 14px 4px 0 11px; }
  .why-box .section-title { font-size: 10.5px; line-height: 11px; margin-bottom: 12px; }
  .why-box .tick-list li { font-size: 9.2px; letter-spacing: -.2px; }
  .review-panel { left: 28px; top: 410px; width: 202px; height: 198px; }
  .review-copy { left: 54px; top: 433px; width: 150px; color: var(--white); font-size: 7.4px; line-height: 9px; }
  .review-copy p + p { margin-top: 6px; }
  .stars { left: 54px; top: 500px; color: var(--yellow); font-size: 11px; letter-spacing: 2px; }
  .recommend-badge { left: 138px; top: 494px; width: 76px; height: 15px; background: var(--yellow); color: var(--ink); font-size: 5.8px; display: flex; align-items: center; justify-content: center; }
  .review-heading { left: 148px; top: 528px; color: var(--white); font-weight: 900; font-style: italic; font-size: 17px; line-height: 16px; letter-spacing: -.6px; }
  .back-logo { left: 28px; top: 657px; font-size: 30px; }
  .back-logo .sub { font-size: 10.5px; margin-top: 2px; }
  .discount-box { left: 190px; top: 630px; width: 145px; height: 118px; border: 1px solid var(--yellow); padding: 15px 0 0 10px; background: var(--white); }
  .discount-label { color: var(--yellow); font-weight: 700; font-size: 9.8px; letter-spacing: -.3px; }
  .discount-amount { color: var(--blue); font-weight: 800; font-size: 17px; margin-top: 6px; letter-spacing: -.4px; }
  .discount-scope { font-weight: 800; font-size: 9.8px; margin-top: 6px; letter-spacing: -.3px; }
  .discount-note { font-weight: 700; font-size: 6.6px; line-height: 8px; margin-top: 12px; }
</style>
</head>
<body>

<div class="stage-label" style="left:207px; top:265px;">MAGNET DESIGN</div>
<div class="stage-label" style="left:585px; top:33px;">DL FLYER FRONT</div>
<div class="stage-label" style="left:963px; top:33px;">DL FLYER BACK</div>

<!-- Magnet -->
<div class="abs magnet">
  <svg class="magnet-frame" width="303" height="303" viewBox="0 0 303 303">
    <polygon points="89,3 214,3 300,89 300,214 214,300 89,300 3,214 3,89" fill="#ffffff" stroke="#2db9e3" stroke-width="6"/>
  </svg>
  <div class="brand-name">VKD<span class="sub">PLUMBING</span></div>
  <div class="magnet-band">SYDNEY'S TRUSTED<br>PLUMBING SPECIALISTS</div>
  <div class="magnet-cta">CALL NOW TO BOOK</div>
  <div class="contact-line" style="left:68px; top:212px;">
    <svg width="16" height="16" viewBox="0 0 24 24"><path fill="#2db9e3" d="M6.6 10.8a15.1 15.1 0 0 0 6.6 6.6l2.2-2.2c.3-.3.7-.4 1-.2 1.1.4 2.3.6 3.6.6.6 0 1 .4 1 1V20c0 .6-.4 1-1 1A17 17 0 0 1 3 4c0-.6.4-1 1-1h3.5c.6 0 1 .4 1 1 0 1.3.2 2.5.6 3.6.1.3 0 .7-.2 1z"/></svg>
    <span class="phone-number" style="font-size:23px;">0491 570 006</span>
  </div>
  <div class="contact-line" style="left:68px; top:245px;">
    <svg width="13" height="10" viewBox="0 0 24 18"><path fill="#2db9e3" d="M0 0h24v2L12 10 0 2zM0 4.5l12 8 12-8V18H0z"/></svg>
    <span class="web-address" style="font-size:13.5px; margin-left:3px;">vkdplumbing.com.au</span>
  </div>
</div>

<!-- DL Flyer Front -->
<section class="flyer flyer-front">
  <div class="abs brand-name front-logo">VKD<span class="sub">PLUMBING</span></div>
  <div class="abs headline-band"></div>
  <div class="photo" role="img" aria-label="Photo of plumber Lachlan in a navy branded polo, arms crossed" style="left:220px; top:37px; width:144px; height:270px; background:linear-gradient(180deg,#c9a48a 0%,#b08a72 20%,var(--photo-navy) 34%,#2a344b 100%); border-radius:60px 60px 0 0;"></div>
  <h1 class="abs headline">BLOCKED<br>DRAIN<br>SPECIAL</h1>
  <div class="abs price-tag">$299</div>

  <div class="abs offer-box">
    <h2 class="offer-title">HIGH PRESSURE<br>WATER JETTING</h2>
    <ul class="drop-list">
      <li>Clear stubborn blocked drains fast.</li>
      <li>Professional high-pressure water jetting.</li>
      <li>Removes tree roots, grease and debris.</li>
    </ul>
  </div>
  <div class="abs bonus-tab">LIMITED TIME BONUS</div>
  <p class="abs bonus-copy">FIRST 15 CALLS RECEIVE<br>A FREE CCTV CAMERA<br>INSPECTION</p>
  <p class="abs bonus-value">(Valued At $149)</p>

  <div class="trust-badge" style="left:28px; top:537px; width:122px; height:42px;">
    <svg width="12" height="15" viewBox="0 0 12 15"><rect x="0.5" y="0.5" width="11" height="14" rx="1.5" fill="none" stroke="#2db9e3"/><path d="M3 4h6M3 7h6M3 10h4" stroke="#2db9e3"/></svg>
    <span>Local Licensed<br>Plumbers</span>
  </div>
  <div class="trust-badge yellow" style="left:160px; top:540px; width:118px; height:39px;">
    <svg width="14" height="14" viewBox="0 0 14 14"><circle cx="7" cy="7.5" r="5.5" fill="none" stroke="#f6c244" stroke-width="1.5"/><path d="M7 4.5V7.5L9 9" stroke="#f6c244" stroke-width="1.3" fill="none"/></svg>
    <span>Fast Same Day<br>Service</span>
  </div>
  <div class="trust-badge yellow" style="left:37px; top:591px; width:113px; height:39px;">
    <svg width="11" height="15" viewBox="0 0 11 15"><rect x="0.5" y="3" width="10" height="11.5" rx="2" fill="#f6c244"/><rect x="3" y="0.5" width="5" height="3" fill="#f6c244"/></svg>
    <span>Upfront Pricing</span>
  </div>
  <div class="trust-badge" style="left:161px; top:591px; width:130px; height:44px;">
    <svg width="20" height="12" viewBox="0 0 20 12"><path fill="#2db9e3" d="M10 0l1.9 3.9 4.3.6-3.1 3 .7 4.3L10 9.8 6.2 11.8l.7-4.3-3.1-3 4.3-.6z"/><circle cx="2.5" cy="8" r="2" fill="#2db9e3"/><circle cx="17.5" cy="8" r="2" fill="#2db9e3"/></svg>
    <span>5 Star Rated<br>Service</span>
  </div>

  <div class="illustration" role="img" aria-label="Illustration of a steel pipe valve with a blue handwheel" style="left:292px; top:560px; width:72px; height:100px; background:linear-gradient(160deg,#eef1f4 0%,var(--steel) 60%,#9aa3ad 100%); border-radius:40px 0 0 30px;"></div>
  <div class="illustration" role="img" aria-label="Illustration of joined steel pipes with a blue valve" style="left:0; top:655px; width:108px; height:116px; background:linear-gradient(90deg,#dfe3e8 0%,var(--steel) 70%,#eef1f4 100%); border-radius:0 40px 0 0;"></div>

  <h2 class="abs cta-title">CALL NOW TO BOOK</h2>
  <p class="abs cta-note">Limited Bookings Available.</p>
  <div class="contact-line" style="left:132px; top:703px;">
    <svg width="16" height="16" viewBox="0 0 24 24"><path fill="#2db9e3" d="M6.6 10.8a15.1 15.1 0 0 0 6.6 6.6l2.2-2.2c.3-.3.7-.4 1-.2 1.1.4 2.3.6 3.6.6.6 0 1 .4 1 1V20c0 .6-.4 1-1 1A17 17 0 0 1 3 4c0-.6.4-1 1-1h3.5c.6 0 1 .4 1 1 0 1.3.2 2.5.6 3.6.1.3 0 .7-.2 1z"/></svg>
    <span class="phone-number" style="font-size:22px;">0491 570 006</span>
  </div>
  <div class="contact-line" style="left:132px; top:733px;">
    <svg width="12" height="9" viewBox="0 0 24 18"><path fill="#2db9e3" d="M0 0h24v2L12 10 0 2zM0 4.5l12 8 12-8V18H0z"/></svg>
    <span class="web-address" style="font-size:13.5px; margin-left:6px;">vkdplumbing.com.au</span>
  </div>
</section>

<!-- DL Flyer Back -->
<section class="flyer flyer-back">
  <div class="abs tag-local">YOUR LOCAL</div>
  <div class="abs tag-trusted">TRUSTED PLUMBER</div>
  <div class="abs intro">
    <p>Fast, Reliable Plumbing Services Across the Sutherland Shire.</p>
    <p>We provide professional plumbing services for homes and businesses including:</p>
  </div>
  <div class="photo" role="img" aria-label="Photo of a plumber fitting a tap at a white basin" style="left:196px; top:37px; width:139px; height:182px; border:1px solid var(--yellow); background:linear-gradient(120deg,var(--photo-light) 0%,#c4c9cf 45%,#2f3a50 65%,#1f2838 100%);"></div>

  <div class="abs services" style="top:222px;">
    <h2 class="section-title" style="margin-bottom:12px;">OUR SERVICES</h2>
    <ul class="tick-list">
      <li><svg width="10" height="9" viewBox="0 0 10 9"><path d="M1 4.5l3 3L9 1" stroke="#2db9e3" stroke-width="1.8" fill="none"/></svg>Blocked Drains</li>
      <li><svg width="10" height="9" viewBox="0 0 10 9"><path d="M1 4.5l3 3L9 1" stroke="#2db9e3" stroke-width="1.8" fill="none"/></svg>Leak Detection &amp; Repairs</li>
      <li><svg width="10" height="9" viewBox="0 0 10 9"><path d="M1 4.5l3 3L9 1" stroke="#2db9e3" stroke-width="1.8" fill="none"/></svg>Hot Water Systems</li>
      <li><svg width="10" height="9" viewBox="0 0 10 9"><path d="M1 4.5l3 3L9 1" stroke="#2db9e3" stroke-width="1.8" fill="none"/></svg>Tap &amp; Toilet Repairs</li>
      <li><svg width="10" height="9" viewBox="0 0 10 9"><path d="M1 4.5l3 3L9 1" stroke="#2db9e3" stroke-width="1.8" fill="none"/></svg>Stormwater Repairs</li>
      <li><svg width="10" height="9" viewBox="0 0 10 9"><path d="M1 4.5l3 3L9 1" stroke="#2db9e3" stroke-width="1.8" fill="none"/></svg>CCTV Drain Inspections</li>
      <li><svg width="10" height="9" viewBox="0 0 10 9"><path d="M1 4.5l3 3L9 1" stroke="#2db9e3" stroke-width="1.8" fill="none"/></svg>Gutter &amp; Roof Plumbing</li>
      <li><svg width="10" height="9" viewBox="0 0 10 9"><path d="M1 4.5l3 3L9 1" stroke="#2db9e3" stroke-width="1.8" fill="none"/></svg>Preventative Plumbing<br>Maintenance</li>
    </ul>
  </div>

  <div class="abs why-box">
    <h2 class="section-title">WHY CHOOSE VKD<br>PLUMBING?</h2>
    <ul class="tick-list">
      <li><svg width="10" height="9" viewBox="0 0 10 9"><path d="M1 4.5l3 3L9 1" stroke="#f6c244" stroke-width="1.8" fill="none"/></svg>Fully Licensed &amp; Insured</li>
      <li><svg width="10" height="9" viewBox="0 0 10 9"><path d="M1 4.5l3 3L9 1" stroke="#f6c244" stroke-width="1.8" fill="none"/></svg>Upfront Honest Pricing</li>
      <li><svg width="10" height="9" viewBox="0 0 10 9"><path d="M1 4.5l3 3L9 1" stroke="#f6c244" stroke-width="1.8" fill="none"/></svg>Fast Local Service</li>
      <li><svg width="10" height="9" viewBox="0 0 10 9"><path d="M1 4.5l3 3L9 1" stroke="#f6c244" stroke-width="1.8" fill="none"/></svg>Clean &amp; Professional</li>
      <li><svg width="10" height="9" viewBox="0 0 10 9"><path d="M1 4.5l3 3L9 1" stroke="#f6c244" stroke-width="1.8" fill="none"/></svg>Workmanship</li>
      <li><svg width="10" height="9" viewBox="0 0 10 9"><path d="M1 4.5l3 3L9 1" stroke="#f6c244" stroke-width="1.8" fill="none"/></svg>Trusted by Local</li>
      <li><svg width="10" height="9" viewBox="0 0 10 9"><path d="M1 4.5l3 3L9 1" stroke="#f6c244" stroke-width="1.8" fill="none"/></svg>Homeowners &amp; Businesses</li>
    </ul>
  </div>

  <svg class="abs review-panel" viewBox="0 0 202 198" aria-hidden="true">
    <path fill="#2db9e3" d="M24 0H178a24 24 0 0 1 24 24V180a18 18 0 0 1-18 18H150c-20 0-40-14-58-28L70 140c-6-5-6-14 0-20 6-5 6-8 0-8H24A24 24 0 0 1 0 88V24A24 24 0 0 1 24 0z"/>
  </svg>
  <div class="illustration" role="img" aria-label="Glossy blue heart icon on a white rounded tile" style="left:68px; top:539px; width:56px; height:56px; border-radius:14px; background:linear-gradient(145deg,#49b8f0,#1a6fd6); border:5px solid #fff;"></div>
  <div class="abs review-copy">
    <p>Lachlan from VKD Plumbing cleared our blocked drain quickly and professionally. Highly recommend!</p>
    <p>Prompt, reliable and great service. Will definitely use again.</p>
  </div>
  <div class="abs stars">★★★★★</div>
  <div class="abs recommend-badge">Highly Recommended</div>
  <div class="abs review-heading">WHAT<br>CLIENT<br>SAY.</div>

  <div class="illustration" role="img" aria-label="Illustration of steel pipework with a blue valve handwheel" style="left:234px; top:454px; width:130px; height:170px; background:linear-gradient(160deg,#f1f3f6 0%,var(--steel) 55%,#98a1ab 100%); border-radius:60px 0 0 50px;"></div>

  <h2 class="abs section-title" style="left:28px; top:630px; font-size:15px;">NEED A PLUMBER?</h2>
  <div class="abs brand-name back-logo">VKD<span class="sub">PLUMBING</span></div>
  <div class="contact-line" style="left:28px; top:703px;">
    <svg width="16" height="16" viewBox="0 0 24 24"><path fill="#2db9e3" d="M6.6 10.8a15.1 15.1 0 0 0 6.6 6.6l2.2-2.2c.3-.3.7-.4 1-.2 1.1.4 2.3.6 3.6.6.6 0 1 .4 1 1V20c0 .6-.4 1-1 1A17 17 0 0 1 3 4c0-.6.4-1 1-1h3.5c.6 0 1 .4 1 1 0 1.3.2 2.5.6 3.6.1.3 0 .7-.2 1z"/></svg>
    <span class="phone-number" style="font-size:20px;">0491 570 006</span>
  </div>
  <div class="contact-line" style="left:28px; top:733px;">
    <svg width="12" height="9" viewBox="0 0 24 18"><path fill="#2db9e3" d="M0 0h24v2L12 10 0 2zM0 4.5l12 8 12-8V18H0z"/></svg>
    <span class="web-address" style="font-size:13px; margin-left:6px;">vkdplumbing.com.au</span>
  </div>

  <div class="abs discount-box">
    <div class="discount-label">NEIGHBOUR DISCOUNT</div>
    <div class="discount-amount">$59 OFF</div>
    <div class="discount-scope">ANY PLUMBING REPAIR</div>
    <div class="discount-note">(MENTION THIS FLYER<br>WHEN BOOKING)</div>
  </div>
</section>

</body>
</html>
```